Funky new Serviced Apartment Company needs a website + logo

Bright Harbor Serviced Lodging is a new company aiming to attract customers who need temporary accommodation (2 days to 6 months) in city locations.

Our customers make considerable savings on longer stays compared to hotels, and have all the creature comforts of home including super-fast WIFI, comfy beds, full kitchen and modern, yet comfortable, furniture.

Another key feature of the design is a page to attract "Partners" who "Work with Us" by allowing us to manage their properties and becoming part of our network of accommodation units. I have include a brochure from one of our competitors, and a video can be found here: http://lnkshort.example/clipz-7 - both can be used as I have permission.

The website design should work on all devices and screen sizes, and lend itself to a mobile app.

We would like to see website designs that are modern and simple, with a strong brand logo. The final design should communicate "Home From Home" and aim to attract professionals away from home on business for long periods of time.

Target Market(s)

Professional People working away from home for extended periods of time

Industry/Entity Type

Accommodation

Contact Information for Business Card

Name, Title, Phone Number, Email
Malcolm Ostby, Owner, 07831 562087, malcolm.ostby@brightharborsl.co.uk

Logo Text

Bright Harbor Service Lodging (Serviced Accommodation optional)

Coding

Coded - Design and coding required

Number of Pages Required

3 page

Font styles to use
Sans Serif

Requirements
Must have
• A 3 page website: Home, Partners, Contact Us
• Home page should have an area to list current apartment units, the user should be able to select a location and filter the list based on price and number of people.
• Partners page should inspire a "Work with us" call to action.
• The design should work with all screen sizes and devices.
• The design should say friendly and professional
Nice to have
• A simple logo, perhaps a smiling face made up using letters 'W' and 'H'.
• A neutral color scheme
Should not have
• No garish or vivid color scheme

```html
<!DOCTYPE html>
<html lang="en">
<head>
<meta charset="utf-8">
<title>Bright Harbor Serviced Lodging</title>
<link href="https://fonts.googleapis.com/css2?family=Poppins:wght@300;400;500;600&display=swap" rel="stylesheet">
<style>
:root{
  --orange:#ff7f45;
  --teal:#1aa393;
  --teal-dark:#14857a;
  --ink:#1d1d1d;
  --text:#555;
  --muted:#9a9a9a;
  --soft-bg:#f6f6f6;
  --line:#e6e6e6;
  --white:#fff;
}
*{box-sizing:border-box;margin:0;padding:0}
html,body{width:1200px;height:2848px;overflow:hidden}
body{font-family:'Poppins',sans-serif;color:var(--ink);background:var(--white);position:relative}
a{color:inherit;text-decoration:none}

/* header */
.site-header{position:absolute;top:0;left:0;width:1200px;height:80px;background:var(--white);box-shadow:0 2px 8px rgba(0,0,0,.06);z-index:2}
.brand{position:absolute;left:88px;top:24px;font-size:23px;font-weight:500;color:var(--ink)}
.main-nav{position:absolute;left:818px;top:0;height:80px;display:flex;align-items:center;gap:40px;font-size:13px;font-weight:500}
.main-nav a{position:relative;height:80px;line-height:80px}
.main-nav a.active{color:var(--muted)}
.main-nav a.active::before{content:"";position:absolute;left:0;right:0;top:0;height:3px;background:var(--teal)}
.menu-toggle{position:absolute;left:1092px;top:31px}

/* hero */
.hero{position:absolute;top:80px;left:0;width:1200px;height:562px;background:linear-gradient(180deg,#c7852f 0%,#e7a23e 35%,#b06a2a 65%,#4a3a33 100%)}
.hero-title{position:absolute;top:196px;width:100%;text-align:center;color:var(--white);font-size:34px;font-weight:400;line-height:40px}
.btn{display:inline-flex;align-items:center;gap:12px;background:var(--orange);color:var(--white);font-size:11px;font-weight:600;letter-spacing:.6px;text-transform:uppercase}
.hero .btn{position:absolute;left:486px;top:302px;height:50px;padding:0 28px}
.hero-dots{position:absolute;top:516px;left:584px;display:flex;gap:7px}
.hero-dots span{width:6px;height:6px;border-radius:50%;background:rgba(255,255,255,.55)}
.hero-dots span:first-child{background:var(--white)}

/* units */
.units{position:absolute;top:642px;left:0;width:1200px;height:1044px;background:var(--soft-bg)}
.section-rule{position:absolute;left:564px;width:72px;height:1px;background:#cfcfcf}
.section-title{position:absolute;width:100%;text-align:center;font-size:27px;font-weight:500}
.filter-bar{position:absolute;left:250px;top:145px;width:700px;height:56px;background:var(--white);box-shadow:0 4px 14px rgba(0,0,0,.07);display:flex;font-size:10px;text-transform:uppercase;letter-spacing:.3px}
.filter-field{flex:0 0 205px;border-right:1px solid var(--line);display:flex;align-items:center;justify-content:space-between;padding:0 22px;color:#444}
.filter-price{flex:1;display:flex;align-items:center;padding:0 22px;color:#bbb;gap:28px}
.filter-price .go{margin-left:auto}
.unit-grid{position:absolute;left:88px;top:245px;display:grid;grid-template-columns:repeat(4,247px);gap:23px 12px}
.unit-card{background:var(--white);height:341px;box-shadow:0 2px 6px rgba(0,0,0,.04)}
.unit-photo{height:192px}
.unit-body{padding:22px 22px 0}
.unit-name{font-size:12px;font-weight:500;text-transform:uppercase;margin-bottom:8px}
.unit-meta{display:flex;align-items:center;gap:6px;font-size:10px;color:var(--muted);margin-bottom:6px}
.unit-link{display:flex;justify-content:flex-end;align-items:center;gap:4px;font-size:10px;font-weight:500;text-transform:uppercase;margin-top:16px}

/* testimonials */
.testimonials{position:absolute;top:1686px;left:0;width:1200px;height:480px;background:var(--white)}
.quote-card{position:absolute;top:200px;width:460px;padding-left:92px}
.avatar{position:absolute;left:0;top:0;width:62px;height:62px;border-radius:50%;border:3px solid #eee}
.quote-name{font-size:15px;font-weight:500;margin-top:4px}
.quote-head{font-size:19px;font-weight:600;margin:4px 0 18px}
.quote-text{font-size:12.5px;color:var(--text);line-height:24px}
.pager{position:absolute;left:1154px;top:265px;display:flex;flex-direction:column;gap:7px}
.pager span{width:6px;height:6px;border-radius:50%;background:#f3c8b3}
.pager span:first-child{background:var(--orange)}

/* call to action */
.cta{position:absolute;top:2166px;left:0;width:1200px;height:268px;background:linear-gradient(90deg,var(--teal) 0%,#2aa89a 50%,var(--teal-dark) 100%)}
.cta-title{position:absolute;left:88px;top:100px;color:var(--white);font-size:28px;font-weight:400;line-height:38px}
.cta .btn{position:absolute;left:880px;top:90px;width:232px;height:88px;padding:0 28px;flex-direction:column;align-items:flex-start;justify-content:center;gap:6px}
.cta .btn small{font-size:11px;font-weight:500;text-transform:none;letter-spacing:0}

/* footer */
.site-footer{position:absolute;top:2434px;left:0;width:1200px;height:414px;background:var(--soft-bg)}
.footer-col{position:absolute;top:74px}
.footer-col h4{font-size:13px;font-weight:400;color:var(--muted);margin-bottom:20px}
.footer-col li{list-style:none;font-size:12.5px;height:37px;display:flex;align-items:flex-start;gap:10px}
.contact-item{display:flex;gap:12px;font-size:12.5px}
.contact-item p{line-height:26px}
.contact-item span{color:var(--muted)}
.contact-rule{width:228px;height:1px;background:var(--line);margin:18px 0 20px}
.dot{width:9px;height:9px;border-radius:50%;background:var(--ink);margin-top:5px}
.copyright{position:absolute;left:0;bottom:0;width:1200px;height:54px;border-top:1px solid var(--line);text-align:center;line-height:54px;font-size:11.5px}
.to-top{position:absolute;left:1136px;top:2806px;width:42px;height:42px;border-radius:50%;background:var(--orange);display:flex;align-items:center;justify-content:center}
</style>
</head>
<body>

<header class="site-header">
  <a class="brand" href="#">Bright Harbor</a>
  <nav class="main-nav">
    <a class="active" href="#">Home</a>
    <a href="#">Partners</a>
    <a href="#">Contact us</a>
  </nav>
  <svg class="menu-toggle" width="20" height="16" viewBox="0 0 20 16"><path d="M0 1h20M0 8h20M4 15h16" stroke="#1d1d1d" stroke-width="2"/></svg>
</header>

<section class="hero" role="img" aria-label="City skyline at sunset with tall office towers">
  <h1 class="hero-title">Bright Harbor<br>Serviced Lodging</h1>
  <a class="btn" href="#">Get in touch with us
    <svg width="18" height="10" viewBox="0 0 18 10"><path d="M0 5h16M12 1l4 4-4 4" stroke="#fff" stroke-width="1.4" fill="none"/></svg>
  </a>
  <div class="hero-dots"><span></span><span></span><span></span></div>
</section>

<section class="units">
  <div class="section-rule" style="top:78px"></div>
  <h2 class="section-title" style="top:88px">Current Appartment Units</h2>
  <form class="filter-bar">
    <div class="filter-field">Location <svg width="7" height="5"><path d="M0 0h7L3.5 5z" fill="#888"/></svg></div>
    <div class="filter-field">Number of people <svg width="7" height="5"><path d="M0 0h7L3.5 5z" fill="#888"/></svg></div>
    <div class="filter-price"><span>Min price</span><span>-</span><span>Max price</span>
      <svg class="go" width="12" height="12" viewBox="0 0 12 12"><circle cx="5" cy="5" r="3.8" stroke="#222" stroke-width="1.6" fill="none"/><path d="M8 8l3.5 3.5" stroke="#222" stroke-width="1.8"/></svg>
    </div>
  </form>

  <div class="unit-grid">
    <article class="unit-card"><div class="unit-photo" role="img" aria-label="Grey bedroom with desk and shelving" style="background:linear-gradient(160deg,#bdbdbd,#5c5c5c)"></div>
      <div class="unit-body"><h3 class="unit-name">Appartment 1</h3>
        <p class="unit-meta"><svg width="8" height="10" viewBox="0 0 8 10"><path d="M4 10S0 6 0 4a4 4 0 018 0c0 2-4 6-4 6z" fill="#ff7f45"/><circle cx="4" cy="4" r="1.4" fill="#fff"/></svg>Some address line goes here</p>
        <p class="unit-meta"><svg width="8" height="9" viewBox="0 0 8 9"><circle cx="4" cy="2.4" r="2.2" fill="#ff7f45"/><path d="M0 9a4 3.6 0 018 0z" fill="#ff7f45"/></svg>5 People allowed</p>
        <a class="unit-link" href="#">View this appartment <svg width="8" height="7"><path d="M0 3.5h7M4 .5l3 3-3 3" stroke="#1d1d1d" fill="none"/></svg></a></div></article>
    <article class="unit-card"><div class="unit-photo" role="img" aria-label="White living room with colourful shelving and wall art" style="background:linear-gradient(160deg,#f1ede8,#c9b9a6)"></div>
      <div class="unit-body"><h3 class="unit-name">Appartment 2</h3>
        <p class="unit-meta"><svg width="8" height="10" viewBox="0 0 8 10"><path d="M4 10S0 6 0 4a4 4 0 018 0c0 2-4 6-4 6z" fill="#ff7f45"/><circle cx="4" cy="4" r="1.4" fill="#fff"/></svg>Some address line goes here</p>
        <p class="unit-meta"><svg width="8" height="9" viewBox="0 0 8 9"><circle cx="4" cy="2.4" r="2.2" fill="#ff7f45"/><path d="M0 9a4 3.6 0 018 0z" fill="#ff7f45"/></svg>5 People allowed</p>
        <a class="unit-link" href="#">View this appartment <svg width="8" height="7"><path d="M0 3.5h7M4 .5l3 3-3 3" stroke="#1d1d1d" fill="none"/></svg></a></div></article>
    <article class="unit-card"><div class="unit-photo" role="img" aria-label="Dark lounge with black sofas" style="background:linear-gradient(160deg,#8d8d8d,#2e2e2e)"></div>
      <div class="unit-body"><h3 class="unit-name">Appartment 3</h3>
        <p class="unit-meta"><svg width="8" height="10" viewBox="0 0 8 10"><path d="M4 10S0 6 0 4a4 4 0 018 0c0 2-4 6-4 6z" fill="#ff7f45"/><circle cx="4" cy="4" r="1.4" fill="#fff"/></svg>Some address line goes here</p>
        <p class="unit-meta"><svg width="8" height="9" viewBox="0 0 8 9"><circle cx="4" cy="2.4" r="2.2" fill="#ff7f45"/><path d="M0 9a4 3.6 0 018 0z" fill="#ff7f45"/></svg>5 People allowed</p>
        <a class="unit-link" href="#">View this appartment <svg width="8" height="7"><path d="M0 3.5h7M4 .5l3 3-3 3" stroke="#1d1d1d" fill="none"/></svg></a></div></article>
    <article class="unit-card"><div class="unit-photo" role="img" aria-label="Bright hotel-style bedroom with large windows" style="background:linear-gradient(160deg,#a9c3d6,#e6e2dc)"></div>
      <div class="unit-body"><h3 class="unit-name">Appartment 4</h3>
        <p class="unit-meta"><svg width="8" height="10" viewBox="0 0 8 10"><path d="M4 10S0 6 0 4a4 4 0 018 0c0 2-4 6-4 6z" fill="#ff7f45"/><circle cx="4" cy="4" r="1.4" fill="#fff"/></svg>Some address line goes here</p>
        <p class="unit-meta"><svg width="8" height="9" viewBox="0 0 8 9"><circle cx="4" cy="2.4" r="2.2" fill="#ff7f45"/><path d="M0 9a4 3.6 0 018 0z" fill="#ff7f45"/></svg>5 People allowed</p>
        <a class="unit-link" href="#">View this appartment <svg width="8" height="7"><path d="M0 3.5h7M4 .5l3 3-3 3" stroke="#1d1d1d" fill="none"/></svg></a></div></article>
    <article class="unit-card"><div class="unit-photo" role="img" aria-label="Warm living room with red door and patterned wall art" style="background:linear-gradient(160deg,#8a5a3c,#d9c3a3)"></div>
      <div class="unit-body"><h3 class="unit-name">Appartment 5</h3>
        <p class="unit-meta"><svg width="8" height="10" viewBox="0 0 8 10"><path d="M4 10S0 6 0 4a4 4 0 018 0c0 2-4 6-4 6z" fill="#ff7f45"/><circle cx="4" cy="4" r="1.4" fill="#fff"/></svg>Some address line goes here</p>
        <p class="unit-meta"><svg width="8" height="9" viewBox="0 0 8 9"><circle cx="4" cy="2.4" r="2.2" fill="#ff7f45"/><path d="M0 9a4 3.6 0 018 0z" fill="#ff7f45"/></svg>5 People allowed</p>
        <a class="unit-link" href="#">View this appartment <svg width="8" height="7"><path d="M0 3.5h7M4 .5l3 3-3 3" stroke="#1d1d1d" fill="none"/></svg></a></div></article>
    <article class="unit-card"><div class="unit-photo" role="img" aria-label="Navy feature wall with white sofa" style="background:linear-gradient(180deg,#20306a 0%,#2c3d7a 55%,#e8e8e8 100%)"></div>
      <div class="unit-body"><h3 class="unit-name">Appartment 6</h3>
        <p class="unit-meta"><svg width="8" height="10" viewBox="0 0 8 10"><path d="M4 10S0 6 0 4a4 4 0 018 0c0 2-4 6-4 6z" fill="#ff7f45"/><circle cx="4" cy="4" r="1.4" fill="#fff"/></svg>Some address line goes here</p>
        <p class="unit-meta"><svg width="8" height="9" viewBox="0 0 8 9"><circle cx="4" cy="2.4" r="2.2" fill="#ff7f45"/><path d="M0 9a4 3.6 0 018 0z" fill="#ff7f45"/></svg>5 People allowed</p>
        <a class="unit-link" href="#">View this appartment <svg width="8" height="7"><path d="M0 3.5h7M4 .5l3 3-3 3" stroke="#1d1d1d" fill="none"/></svg></a></div></article>
    <article class="unit-card"><div class="unit-photo" role="img" aria-label="Neutral bedroom with ceiling fan and dresser" style="background:linear-gradient(160deg,#c9c3bb,#6c6660)"></div>
      <div class="unit-body"><h3 class="unit-name">Appartment 7</h3>
        <p class="unit-meta"><svg width="8" height="10" viewBox="0 0 8 10"><path d="M4 10S0 6 0 4a4 4 0 018 0c0 2-4 6-4 6z" fill="#ff7f45"/><circle cx="4" cy="4" r="1.4" fill="#fff"/></svg>Some address line goes here</p>
        <p class="unit-meta"><svg width="8" height="9" viewBox="0 0 8 9"><circle cx="4" cy="2.4" r="2.2" fill="#ff7f45"/><path d="M0 9a4 3.6 0 018 0z" fill="#ff7f45"/></svg>5 People allowed</p>
        <a class="unit-link" href="#">View this appartment <svg width="8" height="7"><path d="M0 3.5h7M4 .5l3 3-3 3" stroke="#1d1d1d" fill="none"/></svg></a></div></article>
    <article class="unit-card"><div class="unit-photo" role="img" aria-label="Lounge with long red sofa and wooden floor" style="background:linear-gradient(180deg,#eeeae4 0%,#d9d0c8 50%,#c0392b 75%,#a0612f 100%)"></div>
      <div class="unit-body"><h3 class="unit-name">Appartment 8</h3>
        <p class="unit-meta"><svg width="8" height="10" viewBox="0 0 8 10"><path d="M4 10S0 6 0 4a4 4 0 018 0c0 2-4 6-4 6z" fill="#ff7f45"/><circle cx="4" cy="4" r="1.4" fill="#fff"/></svg>Some address line goes here</p>
        <p class="unit-meta"><svg width="8" height="9" viewBox="0 0 8 9"><circle cx="4" cy="2.4" r="2.2" fill="#ff7f45"/><path d="M0 9a4 3.6 0 018 0z" fill="#ff7f45"/></svg>5 People allowed</p>
        <a class="unit-link" href="#">View this appartment <svg width="8" height="7"><path d="M0 3.5h7M4 .5l3 3-3 3" stroke="#1d1d1d" fill="none"/></svg></a></div></article>
  </div>
</section>

<section class="testimonials">
  <div class="section-rule" style="top:80px"></div>
  <h2 class="section-title" style="top:100px">See what our clients say</h2>
  <blockquote class="quote-card" style="left:88px">
    <div class="avatar" role="img" aria-label="Client portrait" style="background:linear-gradient(160deg,#e9d6c8,#b48a70)"></div>
    <p class="quote-name">Nora Lindqvist.</p>
    <p class="quote-head">Dentist came straight to our school!</p>
    <p class="quote-text">"Maecenas tempus tellus eget condimentum rhoncus sem quam semper libero, sit amet adipiscing sem neque sed ipsum nam quam nunc"</p>
  </blockquote>
  <blockquote class="quote-card" style="left:660px">
    <div class="avatar" role="img" aria-label="Client portrait" style="background:linear-gradient(160deg,#d9d2cb,#8a7a6c)"></div>
    <p class="quote-name">Owen Marsh.</p>
    <p class="quote-head">No shock dental bills!</p>
    <p class="quote-text">"Lorem ipsum dolor tempus tellus eget condimentum rhoncus sem quam semper libero, sit amet adipiscing so sem neque sed ipsum nam quam"</p>
  </blockquote>
  <div class="pager"><span></span><span></span><span></span></div>
</section>

<section class="cta" role="img" aria-label="Person in a hat among house plants, tinted teal">
  <h2 class="cta-title">We are looking forward<br>to working with you.</h2>
  <a class="btn" href="#"><small>Contact us</small>
    <span style="display:flex;align-items:center;gap:12px">Get in touch with us <svg width="18" height="10" viewBox="0 0 18 10"><path d="M0 5h16M12 1l4 4-4 4" stroke="#fff" stroke-width="1.4" fill="none"/></svg></span>
  </a>
</section>

<footer class="site-footer">
  <div class="footer-col" style="left:88px"><h4>Quick links</h4>
    <ul><li>Home</li><li>Partners</li><li>Contact us</li></ul></div>
  <div class="footer-col" style="left:361px"><h4>Countries</h4>
    <ul><li>America</li><li>England</li><li>Germany</li><li>France</li><li>Pakistan</li></ul></div>
  <div class="footer-col" style="left:606px"><h4>Keep in touch</h4>
    <div class="contact-item"><svg width="9" height="12" viewBox="0 0 8 10" style="margin-top:6px"><path d="M4 10S0 6 0 4a4 4 0 018 0c0 2-4 6-4 6z" fill="#1aa393"/><circle cx="4" cy="4" r="1.4" fill="#fff"/></svg>
      <p>Address:<br><span>Some address line goes here,<br>City name, Country name</span></p></div>
    <div class="contact-rule" style="margin-left:20px"></div>
    <div class="contact-item"><svg width="10" height="8" viewBox="0 0 10 8" style="margin-top:9px"><rect width="10" height="8" fill="#1aa393"/><path d="M0 0l5 4 5-4" stroke="#fff" fill="none"/></svg>
      <p>Email address:<br><span>info@brightharborsl.co.uk</span></p></div></div>
  <div class="footer-col" style="left:952px"><h4>Follow us</h4>
    <ul><li><i class="dot"></i>Friendsboard</li><li><i class="dot"></i>Chirpline</li><li><i class="dot"></i>Circlespace</li><li><i class="dot"></i>Workmesh</li><li><i class="dot"></i>Clipstream</li></ul></div>
  <p class="copyright">© 2017, All Rights Reserved</p>
</footer>
<a class="to-top" href="#"><svg width="10" height="12" viewBox="0 0 10 12"><path d="M5 12V1M1 5l4-4 4 4" stroke="#fff" stroke-width="1.4" fill="none"/></svg></a>

</body>
</html>
```